landing and results page for local search engine for childrens stuff

bimplo.io is local search engine to find children clothes, bikes, toys, etc locally.

we search thousands of sites tradevast, sellwillow and many more to bring together millions of ads so you can find them all in one place, and organize them with useful features so parents can find local bargains for kids stuff.

the key here is we specialise in finding kids gear, and only bring you results that are local to the user.
look and feel something like this http://www.quorvine.example/
and http://www.tefnar.example/

Target Market(s)

mums, parents , people with kids

Industry/Entity Type

Tradevast

Requirements
Must have
• it must convey that this is a location aware search engine for kids stuff. an image similar to this http://www.plumtwistapp.example/
on landing page

```html
<!DOCTYPE html>
<html lang="en">
<head>
<meta charset="utf-8">
<title>Bimplo – local finds for kids</title>
<link href="https://fonts.googleapis.com/css2?family=Arimo:wght@400;700&display=swap" rel="stylesheet">
<style>
  :root {
    --white: #ffffff;
    --brand-blue: #62b6f2;
    --brand-red: #e0463a;
    --headline-pink: #e07a98;
    --text-grey: #666666;
    --body-grey: #555555;
    --band-blue: #6ec2f9;
    --band-inner: #4da5ec;
    --tile-blue: #dcf0fd;
    --tile-divider: #ffffff;
    --arrow-pink: #d9708d;
    --arrow-green: #8fd08c;
    --arrow-orange: #f1965a;
    --button-top: #fde597;
    --button-bottom: #f5c95a;
    --button-text: #333333;
    --carousel-arrow: #5fb8f4;
  }
  * { box-sizing: border-box; margin: 0; padding: 0; }
  html, body { width: 1200px; height: 980px; overflow: hidden; background: var(--white); }
  body { position: relative; font-family: "Arimo", Arial, sans-serif; color: var(--text-grey); }

  .site-header { position: absolute; left: 0; top: 0; width: 1200px; height: 128px;
    box-shadow: 0 10px 14px -12px rgba(0,0,0,0.18); }
  .brand { position: absolute; left: 430px; top: 36px; display: flex; align-items: center; gap: 14px; }
  .brand-mark { width: 54px; height: 54px; background: var(--brand-red); }
  .brand-name { font-weight: 700; font-size: 54px; color: var(--brand-blue); letter-spacing: 1px; line-height: 1; }

  .hero-photo { position: absolute; left: 200px; top: 190px; width: 530px; height: 410px;
    background: radial-gradient(ellipse at 50% 45%, #f2d9b0 0%, #e9eef6 45%, #ffffff 78%); }

  .hero-copy { position: absolute; left: 751px; top: 230px; width: 380px; }
  .hero-title { font-weight: 700; font-size: 38px; line-height: 39px; color: var(--headline-pink); }
  .hero-text { margin-top: 14px; margin-left: 3px; font-size: 14px; line-height: 19.5px; color: var(--body-grey); width: 366px; }

  .btn { display: flex; align-items: center; justify-content: center; font-size: 14px; color: var(--button-text);
    background: linear-gradient(var(--button-top), var(--button-bottom)); border: 1px solid #e7b957;
    box-shadow: 1px 2px 3px rgba(0,0,0,0.22); text-transform: uppercase; }
  .btn-join { position: absolute; left: 753px; top: 483px; width: 146px; height: 38px; }

  .search-band { position: absolute; left: 43px; top: 599px; width: 1120px; height: 112px; background: var(--band-blue); }
  .search-bar { position: absolute; left: 23px; top: 28px; width: 1073px; height: 60px; background: var(--band-inner); }
  .field { position: absolute; top: 12px; height: 39px; background: var(--white); display: flex; align-items: center; }
  .field-label { padding-left: 12px; font-size: 13px; color: #888; flex: 1; }
  .field-toggle { width: 40px; height: 39px; display: flex; align-items: center; justify-content: center; }
  .field-keyword { left: 12px; width: 288px; } .field-keyword .field-toggle { background: var(--arrow-pink); }
  .field-location { left: 313px; width: 288px; } .field-location .field-toggle { background: var(--arrow-green); }
  .field-gender { left: 616px; width: 288px; } .field-gender .field-toggle { background: var(--arrow-orange); }
  .btn-search { position: absolute; left: 917px; top: 12px; width: 146px; height: 39px; border: none; box-shadow: none; }

  .listings { position: absolute; left: 53px; top: 713px; width: 1099px; height: 159px; background: var(--tile-blue); display: flex; }
  .listing { position: relative; height: 159px; border-right: 2px solid var(--tile-divider); }
  .listing:last-child { border-right: none; }
  .listing-1 { width: 376px; } .listing-2 { width: 375px; } .listing-3 { flex: 1; }
  .listing-image { position: absolute; border-radius: 4px; }
  .listing-text { position: absolute; top: 42px; width: 210px; font-size: 14.3px; line-height: 19.5px; color: var(--text-grey); }
  .listing-1 .listing-image { left: 33px; top: 50px; width: 85px; height: 72px; background: linear-gradient(#4d9ad8, #2e6fb1); }
  .listing-1 .listing-text { left: 139px; }
  .listing-2 .listing-image { left: 28px; top: 42px; width: 80px; height: 86px; background: linear-gradient(#f04a86, #c8235c); }
  .listing-2 .listing-text { left: 124px; }
  .listing-3 .listing-image { left: 24px; top: 38px; width: 68px; height: 92px; background: linear-gradient(#d9c39a 0%, #2f4f84 35%, #1f365f 100%); }
  .listing-3 .listing-text { left: 105px; }
  .carousel-arrow { position: absolute; top: 68px; width: 16px; height: 24px; }
  .carousel-prev { left: 5px; } .carousel-next { right: 5px; }

  .site-footer { position: absolute; left: 0; top: 908px; width: 1200px; text-align: center; }
  .footer-nav { font-size: 14px; color: var(--body-grey); word-spacing: 4px; }
  .footer-nav span { margin: 0 6px; }
  .footer-legal { margin-top: 10px; font-size: 12px; color: var(--body-grey); }
</style>
</head>
<body>
  <header class="site-header">
    <div class="brand">
      <div class="brand-mark"></div>
      <div class="brand-name">Bimplo</div>
    </div>
  </header>

  <section class="hero">
    <div class="hero-photo" role="img" aria-label="Photo of five cheerful children in bright T-shirts and jeans jumping and posing together"></div>
    <div class="hero-copy">
      <h1 class="hero-title">get personalized recommendations for things to do</h1>
      <p class="hero-text">Lorem Ipsum is simply dummy text of the printing and typesetting industry. Lorem Ipsum has been the industry's standard dummy text ever since the 1500s, when an unknown printer took a galley of type and scrambled it to make a type specimen book.</p>
    </div>
    <div class="btn btn-join">Join now</div>
  </section>

  <section class="search-band">
    <div class="search-bar">
      <div class="field field-keyword"><span class="field-label">type a category or keyword</span>
        <span class="field-toggle"><svg width="14" height="11" viewBox="0 0 14 11"><path d="M0 0H14L7 11Z" fill="#a4405d"/></svg></span></div>
      <div class="field field-location"><span class="field-label">location</span>
        <span class="field-toggle"><svg width="14" height="11" viewBox="0 0 14 11"><path d="M0 0H14L7 11Z" fill="#3e8a3c"/></svg></span></div>
      <div class="field field-gender"><span class="field-label">gender</span>
        <span class="field-toggle"><svg width="14" height="11" viewBox="0 0 14 11"><path d="M0 0H14L7 11Z" fill="#b5592b"/></svg></span></div>
      <div class="btn btn-search">Search</div>
    </div>
  </section>

  <section class="listings">
    <div class="listing listing-1">
      <svg class="carousel-arrow carousel-prev" viewBox="0 0 16 24"><path d="M12 3L4 12L12 21" fill="none" stroke="var(--carousel-arrow)" stroke-width="3"/></svg>
      <div class="listing-image" role="img" aria-label="Blue toy train engine"></div>
      <p class="listing-text">Lorem Ipsum is simply dummy text of the printing and typeset-ting industry. Lorem Ipsum has been the industry</p>
    </div>
    <div class="listing listing-2">
      <div class="listing-image" role="img" aria-label="Pink children's hooded jacket"></div>
      <p class="listing-text">Lorem Ipsum is simply dummy text of the printing and typeset-ting industry. Lorem Ipsum has been the industry's standard dummy text</p>
    </div>
    <div class="listing listing-3">
      <div class="listing-image" role="img" aria-label="Toddler denim overalls with striped shirt"></div>
      <p class="listing-text">Lorem Ipsum is simply dummy text of the printing and typeset-ting industry. Lorem Ipsum has been the industry's standard dummy text</p>
      <svg class="carousel-arrow carousel-next" viewBox="0 0 16 24"><path d="M4 3L12 12L4 21" fill="none" stroke="var(--carousel-arrow)" stroke-width="3"/></svg>
    </div>
  </section>

  <footer class="site-footer">
    <nav class="footer-nav">about<span>|</span>press<span>|</span>jobs<span>|</span>team<span>|</span>blog</nav>
    <p class="footer-legal">© 2012 - Terms of Service - Privacy Policy - Program Policies</p>
  </footer>
</body>
</html>
```